Dorvell landscape website

Our company is called Dorvell Landscape, Inc. We are located in Oak Bluffs, Martha's Vineyard Island, MA. We are a design construction maintenance firm offering a wide variety of services. We need to build a website for our Landscape, Construction, and Maintenance Company. The ability to interchange photos in many locations. 6-7 Tabs for individualized services. Ability to change and alter text. Use of our logo to increase branding. Modern, clean, simplified backgrounds are appealing. Possibly black background to allow the colors of flowers and logos to pop. Simplicity in management is of importance! The final design should lend itself to an upscale marketplace.
Updates

Dear Designers, Please be advised that the web design needs coding as well. Coding will not be charged on top of whatever investment and must be inclusive in the package. In short, you will not ask the client for more funds. -ArtFolio Admin (Tomas Ferreira)

Target Market(s)

These are second homeowners. estate type properties. upscale clientele.

Industry/Entity Type

Construction

Requirements
Must have
• multiple tabs 6-7 to be able to highlight services. space for text and photos/albums. easy to navigate.
Should not have
• cheesy gimmicky cheap type feel

```html
<!DOCTYPE html>
<html lang="en">
<head>
<meta charset="utf-8">
<title>Dorvell Landscape Inc.</title>
<link rel="stylesheet" href="https://fonts.googleapis.com/css2?family=Mulish:wght@400;600;700&display=swap">
<style>
:root{
  --green:#4a8a10;
  --green-dark:#3f7a0c;
  --red:#c8281a;
  --ink:#333;
  --muted:#666;
  --panel:#f1f1f1;
  --line:#d9d9d9;
  --black:#000;
}
*{margin:0;padding:0;box-sizing:border-box}
html,body{width:744px;height:1200px;overflow:hidden;background:var(--black);font-family:'Mulish',sans-serif;color:var(--ink)}
.canvas{position:relative;width:744px;height:1200px}
.page{position:absolute;left:37px;top:17px;width:670px;height:1103px;background:#fff}
.abs{position:absolute}
.brand{left:56px;top:28px;width:80px;height:80px;border-radius:50%;background:var(--green);color:#fff;font-weight:700;font-size:13px;letter-spacing:1px;display:flex;align-items:center;justify-content:center;z-index:3}
.phone{right:46px;top:36px;font-size:14px;color:#444;text-align:right}
.phone a,.email a{color:var(--red);text-decoration:none}
.email{right:46px;top:56px;font-size:8.5px;color:#444;text-align:right}
.nav{left:46px;top:86px;width:652px;height:29px;background:var(--green)}
.nav span{position:absolute;top:9px;font-size:8.5px;color:#fff;letter-spacing:.2px}
.hero{left:46px;top:118px;width:652px;height:244px;background:linear-gradient(180deg,#2f4a23 0%,#4d6a35 30%,#8f8a78 55%,#b9b7b0 80%,#cfcdc8 100%);border:1px solid var(--line)}
.hero h1{position:absolute;left:0;right:0;top:92px;text-align:center;color:#fff;font-weight:600;font-size:23px;line-height:29px;text-shadow:0 1px 3px rgba(0,0,0,.5)}
.dot{position:absolute;top:337px;width:8px;height:8px;border-radius:50%;background:#fff}
.dot.on{background:var(--red)}
.svc-img{top:377px;width:205px;height:114px}
.card{top:465px;width:185px;height:93px;background:#f3f3f3;border:1px solid #ddd;text-align:center}
.card h3{margin-top:10px;font-size:11px;font-weight:400;color:var(--green)}
.card p{margin-top:4px;font-size:7px;line-height:13px;color:#555;padding:0 10px}
.more{font-size:7.5px;color:var(--red);letter-spacing:.2px}
.card .more{display:block;margin-top:6px}
.welcome{left:46px;top:577px;width:652px;text-align:center}
.welcome h2{font-size:13.5px;font-weight:400;color:#333}
.welcome h2 b,.sec-title b{font-weight:400;color:var(--green)}
.welcome p{margin-top:8px;font-size:7.2px;line-height:13px;color:#555}
.welcome .more{display:block;margin-top:7px}
.gallery{left:46px;top:680px;width:652px;height:189px;background:var(--panel);border-top:1px solid #e2e2e2}
.gallery h2{position:absolute;top:20px;width:100%;text-align:center;font-size:13.5px;font-weight:400}
.thumb{top:734px;width:149px;height:86px;border:2px solid #fff;box-shadow:0 0 0 1px #ddd}
.gallery-more{left:46px;top:846px;width:652px;text-align:center}
.sec-title{top:888px;font-size:14px;font-weight:400}
.col-text{font-size:7.5px;line-height:13px;color:#555}
.news{left:268px;width:207px;border-bottom:1px solid var(--line);padding-bottom:7px}
.news .date{font-size:7.5px;color:var(--green)}
.news p{margin-top:3px;font-size:7.5px;line-height:13px;color:#555}
.news .more{display:block;margin-top:3px}
.contact{left:491px;top:912px;font-size:7.5px;line-height:15px;color:#555}
.contact .name{color:var(--green);font-weight:600}
.contact a{color:var(--red);text-decoration:none}
.map{left:492px;top:1003px;width:206px;height:96px;background:linear-gradient(90deg,#e9e6df 0%,#e6e3dc 70%,#a9c6e6 100%)}
.footer{left:0;top:1120px;width:744px;height:80px;background:var(--green-dark)}
.foot-brand{left:46px;top:1128px;width:40px;height:40px;border-radius:50%;background:#fff;color:var(--green);font-size:6.5px;font-weight:700;display:flex;align-items:center;justify-content:center}
.copy{left:46px;top:1174px;font-size:7px;color:#e8f0dc}
.connect{left:590px;top:1133px;font-size:8.5px;color:#fff}
.social{top:1150px;width:19px;height:19px;border-radius:50%}
</style>
</head>
<body>
<div class="canvas">
  <div class="page"></div>

  <div class="abs brand">DORVELL</div>
  <div class="abs phone">Telephone: <a>508-555-0142</a></div>
  <div class="abs email">Email: <a>info@dorvelllandscape.com</a></div>

  <nav class="abs nav">
    <span style="left:94px">HOME</span>
    <span style="left:156px">ABOUT US</span>
    <span style="left:236px">SERVICES</span>
    <span style="left:312px">PROJECTS</span>
    <span style="left:392px">GALLERY</span>
    <span style="left:466px">NEWS</span>
    <span style="left:528px">BLOG</span>
    <span style="left:588px">CONTACT US</span>
  </nav>

  <div class="abs hero" role="img" aria-label="Stone garden wall with flowering beds above a stone patio">
    <h1>We are a design construction maintenance firm<br>offering a wide variety of services.</h1>
  </div>
  <span class="dot on" style="left:346px"></span>
  <span class="dot" style="left:361px"></span>
  <span class="dot" style="left:375px"></span>
  <span class="dot" style="left:390px"></span>

  <div class="abs svc-img" style="left:46px;background:linear-gradient(180deg,#8a8f7e 0%,#7b6a4e 45%,#5f9a35 100%)" role="img" aria-label="Wooden deck above a green lawn"></div>
  <div class="abs svc-img" style="left:270px;background:linear-gradient(180deg,#6a5f50 0%,#b88a5a 50%,#8c5f3a 100%)" role="img" aria-label="Timber frame structure under construction"></div>
  <div class="abs svc-img" style="left:492px;background:linear-gradient(180deg,#9fb3c2 0%,#5f7a58 40%,#3f5f2e 100%)" role="img" aria-label="Worker watering a landscape near the water"></div>

  <div class="abs card" style="left:56px"><h3>LANDSCAPE SERVICES</h3><p>Lorem ipsum dolor sit amet, consectetur adipisicing eitseo eiusmod tempor incididunt ut labore et dolore magna aliqua.</p><span class="more">LEARN MORE ››</span></div>
  <div class="abs card" style="left:280px"><h3>CONSTRUCTION SERVICES</h3><p>Lorem ipsum dolor sit amet, consectetur adipisicing eitseo eiusmod tempor incididunt ut labore et dolore magna aliqua.</p><span class="more">LEARN MORE ››</span></div>
  <div class="abs card" style="left:502px"><h3>MAINTENANCE SERVICES</h3><p>Lorem ipsum dolor sit amet, consectetur adipisicing eitseo eiusmod tempor incididunt ut labore et dolore magna aliqua.</p><span class="more">LEARN MORE ››</span></div>

  <section class="abs welcome">
    <h2>WELCOME TO <b>DORVELL LANDSCAPE INC.</b></h2>
    <p>Aliquam molestie, mi et imperdiet euismod, dui purus auctor tellus, et interdum lacus lectus et ante. Sed accumsan sollicitudin sapien, sit amet adipiscing turpis gravida ac.<br>In congue, neque ac lobortis volutpat, libero mauris varius mi, vitae suscipit ipsum ligula vitae risus. Duis aliquam nibh a dui iaculis viverra id a velit. Vivamus egestas risus<br>in magna varius commodo. Sed semper viverra egestas. Etiam pretium porttitor lectus, vel ornare neque porta volutpat.</p>
    <span class="more">LEARN MORE ››</span>
  </section>

  <section class="abs gallery"><h2>PHOTO <b style="font-weight:400;color:var(--green)">GALLERY</b></h2></section>
  <div class="abs thumb" style="left:47px;background:linear-gradient(180deg,#8fb0d0 0%,#4d6a3a 45%,#6b8f45 100%)" role="img" aria-label="Truck moving a large tree"></div>
  <div class="abs thumb" style="left:214px;background:linear-gradient(180deg,#a9b8c4 0%,#7a7266 45%,#6f7a55 100%)" role="img" aria-label="Stone outdoor fireplace"></div>
  <div class="abs thumb" style="left:382px;background:linear-gradient(180deg,#b7c6d4 0%,#8f8070 50%,#b27a45 100%)" role="img" aria-label="House porch with new deck"></div>
  <div class="abs thumb" style="left:549px;background:linear-gradient(180deg,#7a9a60 0%,#5f7080 50%,#4f8a35 100%)" role="img" aria-label="Cottage with lawn"></div>
  <div class="abs gallery-more"><span class="more">CLICK FOR MORE ››</span></div>

  <h2 class="abs sec-title" style="left:46px">OUR <b>PROJECTS</b></h2>
  <h2 class="abs sec-title" style="left:268px">LATEST <b>NEWS</b></h2>
  <h2 class="abs sec-title" style="left:491px">CONTACT <b>INFO</b></h2>

  <div class="abs" style="left:46px;top:916px;width:205px;height:104px;background:linear-gradient(180deg,#8a8c88 0%,#a0784f 50%,#8a6a48 100%)" role="img" aria-label="Wooden forms for a pool foundation"></div>
  <p class="abs col-text" style="left:46px;top:1029px;width:205px">Aliquam molestie, mi et imperdiet euismod, dui purus auctor tellus, et interdum lacus lectus et ante. Sed accumsan sollicitudin sapien, sit amet adipiscing turpis gravida ac. ...</p>
  <span class="abs more" style="left:46px;top:1092px">LEARN MORE ››</span>

  <div class="abs news" style="top:915px"><div class="date">AUG26, 2014</div><p>Aliquam molestie, mi et imperdiet euismod, dui purus auctor tellus, et interdum lacus lectus et ante...</p><span class="more">LEARN MORE ››</span></div>
  <div class="abs news" style="top:982px"><div class="date">AUG26, 2014</div><p>Aliquam molestie, mi et imperdiet euismod, dui purus auctor tellus, et interdum lacus lectus et ante...</p><span class="more">LEARN MORE ››</span></div>
  <div class="abs news" style="top:1049px;border-bottom:none"><div class="date">AUG26, 2014</div><p>Aliquam molestie, mi et imperdiet euismod, dui purus auctor tellus, et interdum lacus lectus et ante...</p><span class="more">LEARN MORE ››</span></div>

  <address class="abs contact" style="font-style:normal">
    <div class="name">DORVELL LANDSCAPE INC.</div>
    <div>P.O. Box 4120, Harbor Point,</div>
    <div>MA 02591</div>
    <div>Ph: <a>508-555-0142</a>, &nbsp; Cell: <a>508-555-0187</a></div>
    <div>Email: <a>info@Dorvell Landscape.com</a></div>
  </address>
  <div class="abs map" role="img" aria-label="Street map of the office location by the harbor"></div>

  <footer class="abs footer"></footer>
  <div class="abs foot-brand">DORVELL</div>
  <div class="abs copy">Copyright © 2014. All Right Reserved &nbsp;|&nbsp; Term of Services</div>
  <div class="abs connect">Connect Us</div>
  <span class="abs social" style="left:591px;background:#3b5a9a"></span>
  <span class="abs social" style="left:615px;background:#2a9fd8"></span>
  <span class="abs social" style="left:640px;background:#555"></span>
  <span class="abs social" style="left:665px;background:#f07a12"></span>
  <span class="abs social" style="left:689px;background:#d8281e"></span>
</div>
</body>
</html>
```